someone who can choose good colours and fonts and a style for an already layed out web page

HI

We need someone who can choose good colors and fonts and style for an already layed out web page.

please look at the first file.

The hard part of what needs to go where is already done,

1) we just need a type of character suitable for our business

2) colors probably in the green / yellow spectrum to suit our business

3) we need you to choose the style. For example you could choose round photos, or square buttons, video boxes with or without frames, that sort of stuff, just tweaking of what is there. plain arial is probably what we'd like but with text but with script or memorable headings. We would just like a design style that you think would be good gor our business model.

4) the twitter,facebook logo needs to be put in a new place

our project is an Italian style village in Italy called "Casale Delle Ginestre", in Abruzzo, Italy.
It is surrounded by vineyards, lake and olive trees.

The most important is that it looks expensive, the village is eco friendly so anything on those lines is great, Obviously Italian, so italian looking characters

our website is www.collinaserena.example but we are updating it. we like the style of the old site , but it is too out of date

you can create the layout using the files we've given below and boxes
Updates

hi we've just updated out brief to make it more simple, its actually not much work its just about design choices

Target Market(s)

all lovers of Italian things
eco frienly

Industry/Entity Type

Business

Font styles to use
Decorative
Script

Colors
fcf9ce
faee3f
fde18a
fece3e
cadf82
9bcb3b
acd036
fce7d2
ec2027

Requirements
Must have
• has to have the same layout or similar so as all the boxes and links are in there
twitter,facebook and other logos need to be present where you want them
Nice to have
• we have chosen some colors but you can choose others 3 or 4 are usual a good number with a light yellow background maybe....
Should not have
• no old style must look up to date

```html
<!DOCTYPE html>
<html lang="en">
<head>
<meta charset="utf-8">
<title>Casale Delle Ginestre</title>
<link href="https://fonts.googleapis.com/css2?family=Open+Sans:wght@400;600;700&display=swap" rel="stylesheet">
<style>
:root{
  --green:#9bcb3b;
  --green-light:#cadf82;
  --green-dark:#5d8a12;
  --cream:#fcf9ce;
  --yellow:#faee3f;
  --gold:#fece3e;
  --peach:#fde18a;
  --blush:#fce7d2;
  --red:#d6202a;
  --text:#555;
  --olive-text:#4a5a0c;
  --dark:#3a3a3a;
}
*{margin:0;padding:0;box-sizing:border-box}
html,body{width:789px;height:1200px;overflow:hidden;background:#fff}
body{font-family:'Open Sans',Arial,sans-serif;color:var(--text);position:relative}
.abs{position:absolute}
.brand-mark{left:66px;top:14px;width:74px;height:74px;background:var(--cream);border:1px solid #eee7a8}
.brand-name{left:150px;top:32px;font-size:26px;font-weight:600;color:var(--dark)}
.social{right:66px;top:21px;display:flex;gap:5px}
.social span{width:19px;height:19px;border-radius:50%;background:#9a9a9a;display:block}
.contact{right:66px;top:53px;text-align:right;font-size:11.5px;line-height:17px;color:#666}
.contact b{font-weight:400;color:var(--green-dark)}
.nav{left:0;top:102px;width:789px;height:31px;background:linear-gradient(#b5db56,var(--green));border-top:1px solid #a6d040}
.nav ul{list-style:none;display:flex;margin-left:66px;height:31px;width:657px;border-left:1px solid #8dbb30}
.nav li{font-size:9.6px;color:#2f4a06;text-transform:uppercase;padding:0 13.5px;line-height:31px;border-right:1px solid #8dbb30}
.nav li.active{background:var(--green-light);padding:0 14.5px}
.hero{left:0;top:133px;width:789px;height:285px;background:linear-gradient(var(--cream),#f7f2b4)}
.map{left:66px;top:142px;width:328px;height:268px;background:linear-gradient(135deg,#d9ecb0,#7fbf3a 55%,#c8e49a);border-radius:2px}
.thumbs{left:397px;top:138px;display:flex;gap:2px}
.thumb{width:63px;text-align:center;font-size:7.2px;color:#333}
.thumb i{display:block;height:70px;margin-bottom:4px}
.gallery{left:397px;top:226px;width:325px;height:187px;background:#333}
.gallery .main{position:absolute;left:4px;top:4px;width:317px;height:134px;background:linear-gradient(#cfdbe4,#8aa85a 40%,#6a8a30)}
.strip{position:absolute;left:20px;top:141px;display:flex;gap:4px}
.strip i{width:44px;height:42px;display:block;background:linear-gradient(#aab8c0,#6e7f45)}
.arrow{position:absolute;top:156px;width:12px;height:12px;border-radius:50%;background:#fff}
.arrow svg{display:block}
h2{font-weight:400;color:var(--red);font-size:18px}
.welcome{left:66px;top:434px;width:657px}
.welcome p{font-size:8.7px;line-height:15.2px;margin-top:6px}
.welcome p+p{margin-top:6px}
.box-news{left:65px;top:575px;width:213px;height:160px;background:linear-gradient(var(--green),#b8d650);padding:7px 11px}
.box-news h3{font-weight:400;font-size:17px;color:#1d2a05}
.box-news p{font-size:7.8px;line-height:12px;color:#2c3c08;margin-top:4px}
.field{height:24px;background:var(--blush);border-radius:3px;margin-top:7px;font-size:8.6px;padding:7px 10px;color:#777}
.submit{position:absolute;right:12px;bottom:10px;background:var(--gold);font-size:9.6px;font-weight:600;color:#6a4a00;padding:4px 7px;border-radius:2px}
.seasons{left:289px;top:575px;width:212px}
.season{height:35px;margin-bottom:7px;display:flex;align-items:center;padding-left:22px;font-weight:700;font-size:13.5px;color:#8a7a30;letter-spacing:.2px}
.season svg{margin-right:12px}
.spring{background:var(--cream)}
.summer{background:var(--yellow)}
.autumn{background:var(--peach)}
.winter{background:var(--gold)}
.box-trip{left:511px;top:575px;width:212px;height:160px;background:var(--green);padding:6px 3px 0}
.box-trip h3{font-weight:400;font-size:17px;color:#1d2a05;padding-left:9px}
.box-trip .photo{position:absolute;left:3px;top:34px;width:206px;height:120px;background:linear-gradient(#b7c0c4,#8a6a3a 45%,#5d4a2c)}
.book{position:absolute;right:12px;bottom:22px;background:var(--gold);font-size:9.6px;color:#6a4a00;padding:4px 7px;border-radius:2px}
.rule{left:66px;top:749px;width:657px;height:1px;background:#ddd}
.col{top:765px;width:212px}
.col h2{margin-bottom:10px}
.col .img{height:103px}
.col p{font-size:9.7px;line-height:15.2px;color:var(--olive-text);margin-top:7px}
.col small{display:block;font-size:8.4px;color:#888;margin-top:2px}
.btn{display:inline-block;margin-top:6px;background:#666;color:#fff;font-size:8.6px;padding:5px 7px;border-radius:2px}
.video{position:relative;height:103px;margin-bottom:6px;background:linear-gradient(#a9b4bf,#5e6650)}
.video svg{position:absolute;left:83px;top:30px}
.more{left:0;top:1033px;width:789px;height:102px;background:linear-gradient(#e4e4e4,#f2f2f2)}
.more .lead{position:absolute;top:22px;width:789px;text-align:center;font-size:9.8px;color:var(--red)}
.more ul{position:absolute;top:48px;list-style:none;font-size:8.8px;line-height:17px;color:#555}
.more li:before{content:"•";color:#999;margin-right:5px}
.foot{left:0;top:1135px;width:789px;height:65px;background:#3e3e3e;color:#ddd;text-align:center}
.foot .links{font-size:8.8px;margin-top:15px;word-spacing:2px}
.foot .links span{color:#999;margin:0 5px}
.foot .copy{font-size:8.8px;margin-top:13px}
</style>
</head>
<body>
<div class="abs brand-mark" aria-hidden="true"></div>
<div class="abs brand-name">Casale Delle Ginestre</div>
<div class="abs social" aria-label="Social links"><span></span><span></span><span></span></div>
<div class="abs contact">Telephone : <b>0850001234</b><br>Address : <b>Via dei Mandorli 12, Colle Verde</b></div>

<nav class="abs nav"><ul>
<li class="active">Home</li><li>About us</li><li>Which reason?</li><li>Description</li><li>Price list</li><li>Testimonials</li><li>Gallery</li><li>Contact us</li>
</ul></nav>

<section class="abs hero"></section>
<div class="abs map" role="img" aria-label="Site plan of the village with phases, lake, olive groves and playground"></div>
<div class="abs thumbs">
 <div class="thumb"><i role="img" aria-label="Sunflower" style="background:linear-gradient(#6aa0d8,#f0c020 60%,#3d7a20)"></i>In the sun</div>
 <div class="thumb"><i role="img" aria-label="Child on the beach" style="background:linear-gradient(#e8d8c0,#d8b890)"></i>By the beach</div>
 <div class="thumb"><i role="img" aria-label="Snowy mountain slope" style="background:linear-gradient(#203a8a,#c9a060)"></i>Ski in mountains</div>
 <div class="thumb" style="width:88px"><i role="img" aria-label="Olive grove" style="background:linear-gradient(#a8c070,#4e6a20)"></i>BBQ in Olive grove</div>
 <div class="thumb" style="width:55px"><i role="img" aria-label="Colosseum in Rome" style="background:linear-gradient(#2c5ab0,#b87a3a)"></i>Near&nbsp;&nbsp; Rome</div>
</div>
<div class="abs gallery">
 <div class="main" role="img" aria-label="Panorama of hills with olive groves and vineyards"></div>
 <span class="arrow" style="left:4px"><svg width="12" height="12"><path d="M7 3 4 6l3 3" fill="none" stroke="#333" stroke-width="1.5"/></svg></span>
 <div class="strip" role="img" aria-label="Gallery thumbnails of the countryside"><i></i><i></i><i></i><i></i><i></i><i></i></div>
 <span class="arrow" style="right:4px"><svg width="12" height="12"><path d="M5 3l3 3-3 3" fill="none" stroke="#333" stroke-width="1.5"/></svg></span>
</div>

<section class="abs welcome">
<h2>Welcome to Casale Delle Ginestre</h2>
<p>Casale Delle Ginestre is built in traditional Italian architectural style and surrounded by olive groves, vineyards, a beautiful lake surrounded by a park with wildlife. The panoramic view of the mountains is breathtaking and you can see for 30 miles on a clear day. Red and white umbrellas, barbeques, swimming pools and a spa will contribute to its unique atmosphere. there will also be a health farm, where you can treat yourself to a luxurious massage.</p>
<p>Ten shops and ensure any of your other needs can be met. Casale Delle Ginestre is ensconced in the beauty of the Italian countryside, where the hot white sandy beaches of the Adriatic coastline meet the cold snowy ski-slopes of the Appenine mountains, with Rome only a short car ride away. Each property will be in the OLD Abruzzo style, with attractive brick and stone walls. There are one-, two- and three-bedroomed apartments and three- or four-bedroomed villas.</p>
</section>

<section class="abs box-news">
<h3>Sign up for Newsletter</h3>
<p>Curabitur luctus pulvinar nunc, non egestas libero pharetra non turpis mi.</p>
<div class="field">Name</div>
<div class="field">E-mail</div>
<span class="submit">SUBMIT</span>
</section>

<section class="abs seasons">
<div class="season spring"><svg width="18" height="18" viewBox="0 0 18 18"><g fill="#8a7a30"><circle cx="9" cy="3.5" r="3"/><circle cx="9" cy="14.5" r="3"/><circle cx="3.5" cy="9" r="3"/><circle cx="14.5" cy="9" r="3"/></g><circle cx="9" cy="9" r="2.2" fill="#fcf9ce"/></svg>PHOTOS OF SPRING</div>
<div class="season summer"><svg width="18" height="18" viewBox="0 0 18 18"><circle cx="9" cy="7" r="6" fill="#8a7a30"/><rect x="8" y="11" width="2" height="6" fill="#8a7a30"/></svg>PHOTOS OF SUMMER</div>
<div class="season autumn"><svg width="18" height="18" viewBox="0 0 18 18"><g fill="#8a7a30"><circle cx="9" cy="3.5" r="3"/><circle cx="9" cy="14.5" r="3"/><circle cx="3.5" cy="9" r="3"/><circle cx="14.5" cy="9" r="3"/></g></svg>PHOTOS OF AUTUMN</div>
<div class="season winter"><svg width="18" height="18" viewBox="0 0 18 18"><g stroke="#8a7a30" stroke-width="1.6"><path d="M9 1v16M1 9h16M3.3 3.3l11.4 11.4M14.7 3.3 3.3 14.7"/></g></svg>PHOTOS OF WINTER</div>
</section>

<section class="abs box-trip">
<h3>Book Trip</h3>
<div class="photo" role="img" aria-label="Lake with reeds and autumn vineyard"></div>
<span class="book">Book Now</span>
</section>

<div class="abs rule"></div>

<section class="abs col" style="left:66px">
<h2>Old Blog</h2>
<div class="img" role="img" aria-label="Dog in a grassy field" style="background:linear-gradient(#b8a890,#6a7a3a)"></div>
<p>Casale Delle Ginestre is built in traditional Italian architectural style and surrounded by olive groves, vineyards, a beautiful lake surrounded by a park with wildlife.</p>
<small>February 8, 2014 &nbsp; at : 10.15 a.m</small>
<span class="btn">View more</span>
</section>
<section class="abs col" style="left:289px">
<h2>New Blog</h2>
<div class="img" role="img" aria-label="Hilltop village with white houses" style="background:linear-gradient(#b8c8d8,#9098a0 60%,#5a6048)"></div>
<p>Casale Delle Ginestre is built in traditional Italian architectural style and surrounded by olive groves, vineyards, a beautiful lake surrounded by a park with wildlife.</p>
<small>February 8, 2014 &nbsp; at : 10.15 a.m</small>
<span class="btn">View more</span>
</section>
<section class="abs col" style="left:511px">
<h2>Videos</h2>
<div class="video" role="img" aria-label="Video of a snowy country lane"><svg width="46" height="46"><circle cx="23" cy="23" r="20" fill="none" stroke="#fff" stroke-width="3.5"/><path d="M18 13v20l15-10z" fill="#fff"/></svg></div>
<div class="video" role="img" aria-label="Video of snowy hills and vineyards"><svg width="46" height="46"><circle cx="23" cy="23" r="20" fill="none" stroke="#fff" stroke-width="3.5"/><path d="M18 13v20l15-10z" fill="#fff"/></svg></div>
</section>

<section class="abs more">
<div class="lead">Find more houses, land, properties for sale and real estate on the following sites:</div>
<ul style="left:74px"><li>VillaSoleggiata (ita)</li><li>VillaSoleggiata (uk)</li></ul>
<ul style="left:216px"><li>VillaSoleggiata (es)</li><li>VillaSoleggiata (de)</li></ul>
<ul style="left:365px"><li>CasaInCollina (en)</li><li>CasaInCollina(ita)</li></ul>
<ul style="left:494px"><li>CasaInCollina (bg)</li><li>CasaInCollina (ru)</li></ul>
<ul style="left:616px"><li>CasaInCollina (de)</li><li>Casale Delle Ginestre (uk)</li></ul>
</section>

<footer class="abs foot">
<div class="links">Home<span>|</span>About us<span>|</span>Which Reason?<span>|</span>Description<span>|</span>Price List<span>|</span>Testimonials<span>|</span>Gallery<span>|</span>Contact us</div>
<div class="copy">Copyright &copy; 2014 &nbsp; Casale Delle Ginestre. &nbsp; All rights reserved.</div>
</footer>
</body>
</html>
```